KRV e-payment Business Card Design

We require a new business card design to suit our expanding consulting business -who are specialists in 2 main areas
1. Advising large Corporations and Government organisation on how to improve the why they use emerging (B2B) electronic payment systems
2. Educate Global and regional banks on how to design, build and market electronic business payment products in emerging markets

Our logo is grey/silver based with a building block theme. It also suggests "insight" and business know-how capitalizing on our KRV name. We also want to engender trust,security and balance via the ying/yan symbol

The design needs to take into account the target regional areas of Australiasia/Asia Pacific/Middle East and Africa

Target Market(s)

Regional Banks and their business customers

Industry/Entity Type

Electronic

Contact Information for Business Card

Marcus Dellwyn
Director KRV Consulting (Aust) Pty Ltd
PO Box 4736
Brambleton NSW 2164
Australia
tel +61 (0) 2 95316407
mob +61 (0) 438275601
krvconsulting@lumenpost.com

```html
<!DOCTYPE html>
<html lang="en">
<head>
<meta charset="utf-8">
<title>KRV e-payment Business Card Design</title>
<link rel="stylesheet" href="https://fonts.googleapis.com/css2?family=Didact+Gothic&display=swap">
<style>
  :root {
    --backdrop: #8d8d8d;
    --silver-light: #ececec;
    --silver-mid: #c9c8c8;
    --silver-dark: #a4a3a3;
    --ink: #141414;
    --ink-soft: #3a3a3a;
    --rule: #1a1a1a;
  }
  * { margin: 0; padding: 0; box-sizing: border-box; }
  html, body {
    width: 1200px; height: 1200px; overflow: hidden;
    background: var(--backdrop);
    font-family: "Didact Gothic", "Century Gothic", sans-serif;
    color: var(--ink);
  }
  .sheet {
    position: relative; width: 1200px; height: 1200px;
    display: flex; flex-direction: column; align-items: center; justify-content: center; gap: 40px;
  }
  .card {
    position: relative; width: 960px; height: 533px;
    background: linear-gradient(180deg,
      var(--silver-mid) 0%, var(--silver-light) 22%, var(--silver-mid) 45%,
      var(--silver-dark) 62%, var(--silver-light) 80%, var(--silver-mid) 100%);
    box-shadow: 0 6px 18px rgba(0,0,0,.35);
  }
  .brand { position: absolute; display: flex; flex-direction: column; }
  .brand-row { display: flex; align-items: center; gap: 14px; }
  .brand-name { color: var(--ink); letter-spacing: .08em; line-height: 1; }
  .brand-dot { border-radius: 50%; background: var(--ink-soft); }
  .brand-tagline { color: var(--ink-soft); margin-top: 10px; }
  .brand-entity { color: var(--ink-soft); }

  /* front */
  .card-front .brand { left: 50%; top: 50%; transform: translate(-50%, -50%); align-items: center; }
  .card-front .brand-name { font-size: 96px; }
  .card-front .brand-dot { width: 34px; height: 34px; }
  .card-front .brand-tagline { font-size: 20px; }
  .card-front .brand-entity { font-size: 18px; margin-top: 6px; }

  /* back */
  .card-back .brand { left: 60px; top: 80px; }
  .card-back .brand-name { font-size: 58px; }
  .card-back .brand-dot { width: 22px; height: 22px; }
  .card-back .brand-tagline { font-size: 14px; margin-top: 8px; }
  .card-back .brand-entity { font-size: 13px; margin-top: 4px; }
  .divider { position: absolute; left: 480px; top: 120px; width: 2px; height: 270px; background: var(--rule); }
  .person { position: absolute; right: 80px; top: 90px; text-align: left; }
  .person-name { font-size: 32px; letter-spacing: .02em; padding-bottom: 2px; border-bottom: 2px solid var(--rule); padding-right: 8px; }
  .person-role { font-size: 19px; margin-top: 2px; }
  .address { position: absolute; left: 60px; top: 340px; width: 400px; font-size: 18px; line-height: 1.4; font-style: normal; }
  .contact { position: absolute; left: 520px; top: 400px; display: grid; grid-template-columns: 90px auto; row-gap: 4px; font-size: 21px; }
  .contact dt { font-weight: 400; }
</style>
</head>
<body>
<main class="sheet">
  <section class="card card-front" aria-label="Card front">
    <div class="brand">
      <div class="brand-row">
        <span class="brand-name">KRV</span>
        <span class="brand-dot" aria-hidden="true"></span>
      </div>
      <p class="brand-tagline">"clear e-payment thinking"</p>
      <p class="brand-entity">Consulting (Australia) Pty Ltd</p>
    </div>
  </section>

  <section class="card card-back" aria-label="Card back">
    <div class="brand">
      <div class="brand-row">
        <span class="brand-name">KRV</span>
        <span class="brand-dot" aria-hidden="true"></span>
      </div>
      <p class="brand-tagline">"clear e-payment thinking"</p>
      <p class="brand-entity">Consulting (Australia) Pty Ltd</p>
    </div>
    <div class="divider" aria-hidden="true"></div>
    <div class="person">
      <p class="person-name">Marcus Dellwyn</p>
      <p class="person-role">-Director</p>
    </div>
    <address class="address">
      KRV Consulting (Aust) Pty Ltd<br>
      PO Box 4736 Brambleton NSW 2164 Australia
    </address>
    <dl class="contact">
      <dt>Tel:</dt><dd>+61 (0) 2 95316407</dd>
      <dt>Mob:</dt><dd>+61 (0) 438275601</dd>
      <dt>Email:</dt><dd>krvconsulting@lumenpost.com</dd>
    </dl>
  </section>
</main>
</body>
</html>
```